card design for engineering consultancy

engineering drafting and project management company the provides drafting services for.
Electrical, Hydraulic, Mechanical, and Civil services
The company is called Q7R Services and logo is as attached
Information on card should be.
1. Logo
2.website : Q7RServices.example
3. email : info@Q7RServices.example
4. Phone: (+61) 400512836
5. Motto: Design - Document - Develop - Deliver

this card should be basically used for business identification only

Target Market(s)

electricians plumbers air conditioning installers and civil contractors

Industry/Entity Type

engineering, drafting, electrical, plumbing, airconditioning, civil

Contact Information for Business Card

1. Logo 2.website : Q7RServices.example 3. email : info@Q7RServices.example 4. Phone: (+61) 400512836 5. Motto: Design - Document - Develop - Deliver

Font styles to use
Serif

Requirements
Must have
• logo
Nice to have
• something inovative and different that makes it stand out from being just another business card

```html
<!DOCTYPE html>
<html lang="en">
<head>
<meta charset="utf-8">
<title>Q7R Services — Business Card</title>
<link href="https://fonts.googleapis.com/css2?family=Cinzel:wght@500;700&family=Montserrat:wght@400&display=swap" rel="stylesheet">
<style>
  :root {
    --backdrop: #151515;
    --card: #1d1d1d;
    --card-edge: #262626;
    --foil: #d9d9d9;
    --foil-dim: #8a8a8a;
    --emboss: #0f0f0f;
    --divider: #3a3a3a;
  }
  html, body {
    margin: 0;
    padding: 0;
    width: 1200px;
    height: 900px;
    overflow: hidden;
    background: var(--backdrop);
  }
  .canvas {
    position: relative;
    width: 1200px;
    height: 900px;
    background: radial-gradient(ellipse at 60% 40%, #222 0%, var(--backdrop) 70%);
  }
  .card {
    position: absolute;
    left: 290px;
    width: 620px;
    height: 354px;
    background: linear-gradient(135deg, var(--card) 0%, #202020 60%, #1a1a1a 100%);
    border: 1px solid var(--card-edge);
    box-shadow: 0 14px 30px rgba(0,0,0,0.6);
    box-sizing: border-box;
  }
  .card--front { top: 60px; }
  .card--back { top: 470px; }

  /* Front */
  .front-brand {
    position: absolute;
    top: 120px;
    left: 0;
    right: 0;
    text-align: center;
    font-family: 'Cinzel', serif;
    font-weight: 700;
    font-size: 50px;
    letter-spacing: 4px;
    color: var(--foil);
  }
  .front-motto {
    position: absolute;
    top: 232px;
    left: 0;
    right: 0;
    text-align: center;
    font-family: 'Cinzel', serif;
    font-weight: 700;
    font-size: 17px;
    letter-spacing: 1px;
    color: var(--foil-dim);
  }

  /* Back */
  .back-brand {
    position: absolute;
    left: 40px;
    top: 150px;
    width: 220px;
    text-align: center;
    font-family: 'Cinzel', serif;
    font-weight: 700;
    font-size: 34px;
    letter-spacing: 2px;
    color: var(--emboss);
    text-transform: uppercase;
  }
  .back-divider {
    position: absolute;
    left: 290px;
    top: 110px;
    width: 1px;
    height: 140px;
    background: var(--divider);
  }
  .contact {
    position: absolute;
    left: 320px;
    top: 118px;
  }
  .contact__name {
    font-family: 'Cinzel', serif;
    font-weight: 700;
    font-size: 30px;
    color: var(--foil);
    margin: 0 0 14px;
    letter-spacing: 1px;
  }
  .contact__list {
    list-style: none;
    margin: 0;
    padding: 0;
    font-family: 'Montserrat', sans-serif;
    font-size: 16px;
    color: var(--foil);
  }
  .contact__list li {
    display: flex;
    align-items: center;
    gap: 10px;
    margin-bottom: 7px;
  }
  .contact__icon {
    width: 14px;
    height: 14px;
    flex: none;
    stroke: var(--foil-dim);
    fill: none;
    stroke-width: 1.5;
  }
</style>
</head>
<body>
<main class="canvas">
  <section class="card card--front">
    <div class="front-brand">Q7R SERVICES</div>
    <div class="front-motto">DESIGN | DOCUMENT | DEVELOP | DELIVER</div>
  </section>

  <section class="card card--back">
    <div class="back-brand">Q7R Services</div>
    <div class="back-divider"></div>
    <div class="contact">
      <h1 class="contact__name">ALEX MORGAN</h1>
      <ul class="contact__list">
        <li>
          <svg class="contact__icon" viewBox="0 0 16 16"><path d="M4 1.5 L6.5 4.5 L5 6.5 Q6.5 9.5 9.5 11 L11.5 9.5 L14.5 12 L12.5 14.5 Q6 14 1.5 3.5 Z"/></svg>
          (+61) 400512836
        </li>
        <li>
          <svg class="contact__icon" viewBox="0 0 16 16"><rect x="1.5" y="3.5" width="13" height="9"/><path d="M1.5 3.5 L8 9 L14.5 3.5"/></svg>
          info@Q7RServices.example
        </li>
        <li>
          <svg class="contact__icon" viewBox="0 0 16 16"><circle cx="8" cy="8" r="6.5"/><ellipse cx="8" cy="8" rx="3" ry="6.5"/><path d="M1.5 8 H14.5"/></svg>
          www.Q7RServices.example
        </li>
      </ul>
    </div>
  </section>
</main>
</body>
</html>
```